Construction company focused on concrete and shed construction.

We need to update our current business card for ridgeforgebuilds.com.au we would like an eye catching design with blue, grey and white incorporating our current logo.
Our company started off in concreting and due to varying factors we have expanded to include shed construction as well.
This has led to our current Logo looking a little out of place and somehow need to use the card to bring in the shed construction side of the business while not having to change current concrete look "KESTRO" logo as we already have this incorporated into our company clothing and are not willing to change this yet.
Photo image attached for inspiration/ visual reference of type of work, not to be used on final design.
Please no cheesy designs of men in hard hats and tools
Final design should demonstrate a modern and service focused company.

Target Market(s)

Farmers, Business owners, Developers, Architects, Commercial project delivery

Industry/Entity Type

Construction Company

Contact Information for Business Card

Kestro Constructions.
7b Harlow st
South Launceston Tas
03 62918873

Font styles to use
Other font styles liked:
• see font in logo

Colors
3176b5
b2b2b2

Requirements
Must have
• Easy to read font,
• good contrast between back ground and writing
Nice to have
• Modern and corporate look with a fun but professional image.
Should not have
• Comic images or shadow images of tools/ people.

```html
<!DOCTYPE html>
<html lang="en">
<head>
<meta charset="utf-8">
<title>Kestro Constructions – Business Card</title>
<link href="https://fonts.googleapis.com/css2?family=Graduate&family=Raleway:wght@400&family=Arimo:wght@400;700&display=swap" rel="stylesheet">
<style>
  :root {
    --brand-blue: #1b6a9d;
    --ink-blue: #1d6aa8;
    --logo-grey: #8f959b;
    --text-grey: #6d6d6d;
    --card-white: #ffffff;
    --stage: #2b2b2d;
  }
  * { box-sizing: border-box; margin: 0; padding: 0; }
  html, body { width: 1200px; height: 880px; overflow: hidden; }
  body { background: var(--stage); position: relative; font-family: "Arimo", Arial, sans-serif; }

  .card {
    position: absolute;
    width: 620px;
    height: 354px;
    border-radius: 22px;
  }

  /* Front side */
  .card--front {
    left: 60px; top: 60px;
    background: var(--brand-blue);
    color: var(--card-white);
    text-align: center;
  }
  .front__title {
    position: absolute;
    left: 0; right: 0; top: 128px;
    font-family: "Graduate", Georgia, serif;
    font-size: 46px;
    letter-spacing: 1px;
    line-height: 1;
  }
  .front__web {
    position: absolute;
    left: 0; right: 0; top: 200px;
    font-family: "Raleway", Arial, sans-serif;
    font-size: 15px;
    letter-spacing: 3.5px;
  }

  /* Back side */
  .card--back {
    left: 520px; top: 466px;
    background: var(--card-white);
  }
  .brand-mark {
    position: absolute;
    left: 418px; top: 32px;
    width: 160px; height: 130px;
    display: flex; flex-direction: column; align-items: center; justify-content: center; gap: 10px;
  }
  .brand-mark__dot {
    width: 70px; height: 70px; border-radius: 50%;
    background: var(--logo-grey);
  }
  .brand-mark__name {
    font-family: "Arimo", Arial, sans-serif;
    font-weight: 700;
    font-size: 24px;
    letter-spacing: 1px;
    color: var(--ink-blue);
  }

  .social {
    position: absolute;
    left: 508px; top: 198px;
    display: flex; gap: 8px;
  }
  .social__tile { width: 24px; height: 24px; border-radius: 3px; background: var(--ink-blue); }

  .person { position: absolute; left: 38px; top: 212px; }
  .person__name { font-weight: 700; font-size: 19px; color: var(--ink-blue); line-height: 1.05; }
  .person__role { font-size: 15px; color: var(--text-grey); line-height: 1.1; }

  .contact {
    position: absolute;
    display: flex; align-items: center; gap: 7px;
    font-size: 15px; color: var(--text-grey);
  }
  .contact svg { width: 18px; height: 18px; flex: none; }
  .contact--phone { left: 60px; top: 270px; }
  .contact--web { left: 60px; top: 293px; }
  .contact--address { left: 60px; top: 316px; }
  .contact--email { left: 252px; top: 232px; }
</style>
</head>
<body>

<section class="card card--front">
  <h1 class="front__title">KESTRO CONSTRUCTIONS</h1>
  <p class="front__web">ridgeforgebuilds.com.au</p>
</section>

<section class="card card--back">
  <div class="brand-mark">
    <span class="brand-mark__dot"></span>
    <span class="brand-mark__name">KESTRO</span>
  </div>

  <div class="social" aria-label="Social links">
    <span class="social__tile"></span>
    <span class="social__tile"></span>
    <span class="social__tile"></span>
  </div>

  <div class="person">
    <p class="person__name">LIAM HARTE</p>
    <p class="person__role">Project Manager</p>
  </div>

  <p class="contact contact--email">
    <svg viewBox="0 0 20 20" aria-hidden="true"><circle cx="10" cy="10" r="8.5" fill="none" stroke="#1d6aa8" stroke-width="1.6"/><rect x="5.5" y="7" width="9" height="6" fill="none" stroke="#1d6aa8" stroke-width="1.3"/><path d="M5.5 7 L10 10.5 L14.5 7" fill="none" stroke="#1d6aa8" stroke-width="1.3"/></svg>
    admin@ridgeforgebuilds.com.au
  </p>
  <p class="contact contact--phone">
    <svg viewBox="0 0 20 20" aria-hidden="true"><circle cx="10" cy="10" r="8.5" fill="none" stroke="#1d6aa8" stroke-width="1.6"/><path d="M7 5.5 L8.6 7.6 L7.8 8.8 Q9 11.4 11.2 12.2 L12.4 11.4 L14.5 13 L13.4 14.5 Q8.5 14 5.6 7 Z" fill="#1d6aa8"/></svg>
    03 62918873
  </p>
  <p class="contact contact--web">
    <svg viewBox="0 0 20 20" aria-hidden="true"><circle cx="10" cy="10" r="8.5" fill="none" stroke="#1d6aa8" stroke-width="1.6"/><circle cx="10" cy="10" r="5" fill="none" stroke="#1d6aa8" stroke-width="1.2"/><ellipse cx="10" cy="10" rx="2.2" ry="5" fill="none" stroke="#1d6aa8" stroke-width="1"/><path d="M5 10 H15" stroke="#1d6aa8" stroke-width="1"/></svg>
    ridgeforgebuilds.com.au
  </p>
  <p class="contact contact--address">
    <svg viewBox="0 0 20 20" aria-hidden="true"><circle cx="10" cy="10" r="8.5" fill="none" stroke="#1d6aa8" stroke-width="1.6"/><path d="M10 15 Q6 10.5 6 8.5 A4 4 0 0 1 14 8.5 Q14 10.5 10 15 Z" fill="none" stroke="#1d6aa8" stroke-width="1.3"/><circle cx="10" cy="8.5" r="1.3" fill="#1d6aa8"/></svg>
    7b Harlow st. South Launceston Tas
  </p>
</section>

</body>
</html>
```